New Business Card Design Project

We require a business card design for Zelvaquin, a newly established Indian company.
Our focus is on the development, manufacturing, and export of a diverse array of pharmaceutical products on a global scale. The card should convey a professional appearance, as our primary markets are in Africa, China, and Southeast Asian nations.
We envision a two-sided business card, with the reverse side dedicated to a logo set against a solid color or an elegantly designed pattern. The corners should be rounded. We would appreciate seeing both horizontal and vertical design options. We trust the designer to utilize their expertise in creating this design.

The content for the business card is included in the attached Word file.

Target Market(s)

Our primary markets are in Africa, China, and Southeast Asian, Latin America, Maldives, Sri Lanka

Industry/Entity Type

Pharmaceutical Manufacturing and Export

Contact Information for Business Card

Colors

Designer to choose colors to be used in the design.

Requirements
Must have
• The reverse side of the business card features solely the logo along with the tagline, "Wellness in Bloom."
Should not have
• The logo should not exceed two instances, encompassing both the front and back sides of the card.

```html
<!DOCTYPE html>
<html lang="en">
<head>
<meta charset="utf-8">
<title>Zelvaquin Business Card</title>
<link rel="stylesheet" href="https://fonts.googleapis.com/css2?family=Poppins:wght@400;500;700&display=swap">
<style>
  :root {
    --stage: #1e1e1e;
    --card-white: #ffffff;
    --card-white-shade: #ececec;
    --brand-blue: #29a9e1;
    --brand-blue-light: #3cc4fa;
    --ink-dark: #1c1c1c;
    --ink-light: #ffffff;
  }
  * { box-sizing: border-box; margin: 0; padding: 0; }
  html, body {
    width: 1200px;
    height: 1015px;
    overflow: hidden;
  }
  body {
    background: var(--stage);
    font-family: "Poppins", sans-serif;
    position: relative;
  }
  .card {
    position: absolute;
    width: 520px;
    height: 300px;
    border-radius: 22px;
    overflow: hidden;
  }
  .card-logo-side {
    left: 60px;
    top: 220px;
    background: linear-gradient(160deg, var(--card-white) 0%, var(--card-white) 45%, var(--card-white-shade) 100%);
    display: flex;
    flex-direction: column;
    align-items: center;
    justify-content: center;
  }
  .brand-lockup {
    display: flex;
    align-items: center;
    gap: 14px;
  }
  .brand-dot {
    width: 22px;
    height: 22px;
    border-radius: 50%;
    background: var(--brand-blue);
  }
  .brand-name {
    font-weight: 700;
    font-size: 52px;
    color: var(--brand-blue);
    letter-spacing: 0.5px;
    line-height: 1;
  }
  .brand-tagline {
    margin-top: 10px;
    font-weight: 400;
    font-size: 19px;
    color: var(--ink-dark);
    letter-spacing: 1px;
  }
  .card-contact-side {
    left: 620px;
    top: 495px;
    background: linear-gradient(160deg, var(--brand-blue-light) 0%, var(--brand-blue) 100%);
    color: var(--ink-light);
  }
  .holder {
    position: absolute;
    left: 34px;
    top: 36px;
  }
  .holder-name {
    font-weight: 700;
    font-size: 21px;
    letter-spacing: 1.2px;
    text-transform: uppercase;
  }
  .holder-role {
    font-size: 13px;
    line-height: 1.35;
    margin-top: 2px;
  }
  .contact-list {
    position: absolute;
    left: 34px;
    bottom: 32px;
    list-style: none;
    font-size: 14px;
    line-height: 1.55;
  }
  .contact-list li {
    display: flex;
    align-items: center;
    gap: 10px;
  }
  .contact-list svg {
    width: 14px;
    height: 14px;
    flex: none;
  }
  .address {
    position: absolute;
    right: 34px;
    top: 150px;
    text-align: right;
    font-size: 14px;
    line-height: 1.45;
    font-style: normal;
  }
</style>
</head>
<body>
  <section class="card card-logo-side">
    <div class="brand-lockup">
      <span class="brand-dot"></span>
      <span class="brand-name">Zelvaquin</span>
    </div>
    <p class="brand-tagline">Wellness in Bloom.</p>
  </section>

  <section class="card card-contact-side">
    <div class="holder">
      <h1 class="holder-name">Rohan K. Sethwal</h1>
      <p class="holder-role">CEO<br>Zelvaquin</p>
    </div>

    <ul class="contact-list">
      <li>
        <svg viewBox="0 0 24 24" fill="none" stroke="currentColor" stroke-width="2.2" stroke-linecap="round" stroke-linejoin="round"><path d="M22 16.9v3a2 2 0 0 1-2.2 2 19.8 19.8 0 0 1-8.6-3.1 19.5 19.5 0 0 1-6-6A19.8 19.8 0 0 1 2.1 4.2 2 2 0 0 1 4.1 2h3a2 2 0 0 1 2 1.7c.1.9.4 1.8.7 2.7a2 2 0 0 1-.5 2.1L8 9.8a16 16 0 0 0 6 6l1.3-1.3a2 2 0 0 1 2.1-.4c.9.3 1.8.6 2.7.7a2 2 0 0 1 1.7 2z"/></svg>
        +919800011234
      </li>
      <li>
        <svg viewBox="0 0 24 24" fill="none" stroke="currentColor" stroke-width="2.2" stroke-linejoin="round"><rect x="2" y="5" width="20" height="14" rx="1.5"/><path d="M2 6l10 7 10-7"/></svg>
        rsethwal@zelvaquin.com
      </li>
      <li>
        <svg viewBox="0 0 24 24" fill="none" stroke="currentColor" stroke-width="2"><circle cx="12" cy="12" r="10"/><path d="M2 12h20M12 2c3 3 3 17 0 20M12 2c-3 3-3 17 0 20"/></svg>
        https://zelvaquin.com/
      </li>
    </ul>

    <address class="address">
      12, Kamal Vihar<br>
      Nashik, 422001, India
    </address>
  </section>
</body>
</html>
```